Consulting Company Business Card

I am looking for a minimalist, classy, professional design on my business card. I would like it to be double-sided. I want to use the font and color scheme of my logo which are attached. Please be creative in the designs that you send me. I want to play off the design of my logo with the inner C that is Green and Blue broken up with the white.
Target Market(s)
Small Businesses
Industry/Entity Type
Consulting
Contact Information for Business Card
Derek L. Whitmore, CPA CGMA, 555-014-2283, dwhitmore@brovantadvisory.example, www.brovantadvisory.example

```html
<!DOCTYPE html>
<html lang="en">
<head>
<meta charset="utf-8">
<title>Brovant Advisory – Business Card</title>
<link rel="stylesheet" href="https://fonts.googleapis.com/css2?family=Montserrat:wght@400;500;700;800&display=swap">
<style>
  :root {
    --navy: #262c55;
    --teal: #23868a;
    --ink: #1d1f2a;
    --paper: #ffffff;
    --stage: #e9eaec;
  }
  * { margin: 0; padding: 0; box-sizing: border-box; }
  html, body {
    width: 1200px;
    height: 900px;
    overflow: hidden;
    background: var(--stage);
    font-family: "Montserrat", Arial, sans-serif;
  }
  .canvas {
    position: relative;
    width: 1200px;
    height: 900px;
  }
  .card {
    position: absolute;
    left: 260px;
    width: 680px;
    height: 388px;
    background: var(--paper);
    box-shadow: 0 6px 18px rgba(0,0,0,0.12);
    overflow: hidden;
  }
  .card--front { top: 50px; }
  .card--back { top: 462px; }

  .brand {
    display: flex;
    align-items: center;
    gap: 16px;
    color: var(--navy);
    font-weight: 800;
    text-transform: uppercase;
    letter-spacing: 0.04em;
    line-height: 1.05;
  }
  .brand__dot {
    width: 24px;
    height: 24px;
    border-radius: 50%;
    background: var(--navy);
    flex: none;
  }
  .brand__name span { display: block; }
  .card--front .brand {
    position: absolute;
    inset: 0;
    justify-content: center;
    font-size: 48px;
  }
  .card--back .brand {
    position: absolute;
    left: 48px;
    top: 110px;
    width: 220px;
    font-size: 30px;
  }

  .divider {
    position: absolute;
    left: 288px;
    top: 70px;
    width: 2px;
    height: 150px;
    background: var(--teal);
  }
  .contact {
    position: absolute;
    left: 312px;
    top: 66px;
    color: var(--ink);
  }
  .contact__name {
    color: var(--teal);
    font-weight: 800;
    font-size: 21px;
    line-height: 1.1;
    text-transform: uppercase;
    letter-spacing: 0.01em;
  }
  .contact__title {
    font-size: 16px;
    font-weight: 500;
    margin-top: 3px;
  }
  .contact__list {
    list-style: none;
    margin-top: 16px;
  }
  .contact__item {
    display: flex;
    align-items: center;
    gap: 10px;
    font-size: 13px;
    line-height: 1;
    margin-bottom: 10px;
  }
  .contact__icon {
    width: 16px;
    height: 16px;
    flex: none;
  }
  .swoosh {
    position: absolute;
    left: 0;
    top: 0;
    width: 680px;
    height: 388px;
  }
</style>
</head>
<body>
<main class="canvas">

  <section class="card card--front" aria-label="Card front">
    <div class="brand"><span class="brand__dot"></span><span class="brand__name">Brovant Advisory</span></div>
  </section>

  <section class="card card--back" aria-label="Card back">
    <svg class="swoosh" viewBox="0 0 680 388" aria-hidden="true">
      <path d="M0,372 C320,347 600,302 680,142 L680,388 L0,388 Z" fill="var(--teal)"/>
      <path d="M0,362 C320,337 598,292 670,134" fill="none" stroke="var(--paper)" stroke-width="12"/>
      <path d="M0,358 C320,333 596,288 666,130" fill="none" stroke="var(--navy)" stroke-width="7" stroke-linecap="round"/>
    </svg>

    <div class="brand"><span class="brand__dot"></span><span class="brand__name"><span>Brovant</span><span>Advisory</span></span></div>

    <div class="divider"></div>

    <div class="contact">
      <h1 class="contact__name">Derek L. Whitmore</h1>
      <p class="contact__title">CPA CGMA</p>
      <ul class="contact__list">
        <li class="contact__item">
          <svg class="contact__icon" viewBox="0 0 24 24" aria-hidden="true"><path d="M6.6 10.8a15 15 0 0 0 6.6 6.6l2.2-2.2a1 1 0 0 1 1-.25 11.4 11.4 0 0 0 3.6.57 1 1 0 0 1 1 1V20a1 1 0 0 1-1 1A17 17 0 0 1 3 4a1 1 0 0 1 1-1h3.5a1 1 0 0 1 1 1c0 1.25.2 2.45.57 3.57a1 1 0 0 1-.25 1z" fill="var(--teal)"/></svg>
          <span>555-014-2283</span>
        </li>
        <li class="contact__item">
          <svg class="contact__icon" viewBox="0 0 24 24" aria-hidden="true"><rect x="2" y="5" width="20" height="14" rx="1.5" fill="var(--navy)"/><path d="M3 6l9 7 9-7" fill="none" stroke="var(--paper)" stroke-width="1.6"/></svg>
          <span>dwhitmore@brovantadvisory.example</span>
        </li>
        <li class="contact__item">
          <svg class="contact__icon" viewBox="0 0 24 24" aria-hidden="true"><circle cx="12" cy="12" r="10" fill="var(--teal)"/><path d="M2 12h20M12 2c3 3 3 17 0 20M12 2c-3 3-3 17 0 20" fill="none" stroke="var(--paper)" stroke-width="1.4"/></svg>
          <span>www.brovantadvisory.example</span>
        </li>
      </ul>
    </div>
  </section>

</main>
</body>
</html>
```